BKA

Please send us some options for letterhead I attached our Logo. In addition to the Logo we need this information somewhere on the page

47 Fenbury Lane
Millbrook, CT 06512
203-481-7629

```html
<!DOCTYPE html>
<html lang="en">
<head>
<meta charset="utf-8">
<title>BKA Letterhead</title>
<link rel="stylesheet" href="https://fonts.googleapis.com/css2?family=Source+Sans+3:wght@400;600;700&display=swap">
<style>
  :root {
    --paper: #ffffff;
    --ink: #2e2a2b;
    --brand-dark: #4a4142;
    --brand-blue: #1f7fc4;
    --rule: #8a8a8a;
  }
  * { margin: 0; padding: 0; box-sizing: border-box; }
  html, body {
    width: 964px;
    height: 1200px;
    overflow: hidden;
    background: var(--paper);
  }
  .letterhead {
    position: relative;
    width: 964px;
    height: 1200px;
    background: var(--paper);
    font-family: "Source Sans 3", "Myriad Pro", Arial, sans-serif;
    color: var(--ink);
  }
  .brand {
    position: absolute;
    left: 32px;
    top: 42px;
    display: flex;
    align-items: center;
    gap: 14px;
  }
  .brand-mark {
    width: 22px;
    height: 22px;
    background: var(--brand-blue);
  }
  .brand-name {
    font-size: 54px;
    font-weight: 700;
    letter-spacing: 1px;
    line-height: 1;
    color: var(--brand-dark);
  }
  .address {
    position: absolute;
    left: 766px;
    top: 72px;
    padding-left: 12px;
    border-left: 2px solid var(--rule);
    font-size: 17px;
    font-style: normal;
    line-height: 27px;
    color: var(--ink);
  }
  .contact {
    position: absolute;
    left: 38px;
    top: 1128px;
    list-style: none;
    font-size: 17px;
    line-height: 27px;
    color: var(--ink);
  }
  .contact li {
    display: flex;
    align-items: center;
    gap: 6px;
  }
  .contact svg {
    width: 14px;
    height: 14px;
    flex: none;
  }
</style>
</head>
<body>
  <main class="letterhead">
    <header>
      <div class="brand">
        <span class="brand-mark"></span>
        <span class="brand-name">BKA</span>
      </div>
      <address class="address">
        47 Fenbury Lane<br>
        Millbrook, CT 06512
      </address>
    </header>

    <footer>
      <ul class="contact">
        <li>
          <svg viewBox="0 0 14 14" aria-hidden="true">
            <circle cx="7" cy="7" r="6" fill="none" stroke="var(--brand-blue)" stroke-width="1.4"/>
            <path d="M5 3.8 L6.2 5.6 L5.4 6.4 Q6.3 8 7.6 8.6 L8.4 7.8 L10.2 9 L9.4 10.2 Q6 9.8 3.8 5 Z" fill="var(--brand-blue)"/>
          </svg>
          <span>203-481-7629</span>
        </li>
        <li>
          <svg viewBox="0 0 14 14" aria-hidden="true">
            <circle cx="7" cy="7" r="6" fill="var(--brand-blue)"/>
            <g fill="none" stroke="#ffffff" stroke-width="0.8">
              <ellipse cx="7" cy="7" rx="2.6" ry="6"/>
              <line x1="1" y1="7" x2="13" y2="7"/>
              <line x1="2" y1="4.2" x2="12" y2="4.2"/>
              <line x1="2" y1="9.8" x2="12" y2="9.8"/>
            </g>
          </svg>
          <span>www.bka.org</span>
        </li>
      </ul>
    </footer>
  </main>
</body>
</html>
```